PELTON RIDGE HEATING AND COOLING

Industry/Entity Type

Hvac

Requirements
Must have
• logo
My name: Doug Ferriblen
Phone number 555-304-9461
Text:
Furnace and AC repairs
New furnace and AC installation
Ductwork
Gas lines
Water Tanks
Tankless water heaters
Nice to have
• Profesional modern look

```html
<!DOCTYPE html>
<html lang="en">
<head>
<meta charset="utf-8">
<title>Pelton Ridge Heating and Cooling – Business Card</title>
<link rel="stylesheet" href="https://fonts.googleapis.com/css2?family=Cinzel:wght@600&family=Arimo:wght@400;700&display=swap">
<style>
  :root {
    --backdrop: #2e2e30;
    --card: #f4f4f2;
    --brand-blue: #1f4f9a;
    --band-blue: #174a96;
    --accent-red: #d42a2a;
    --ink-grey: #6e6e6e;
    --band-text: #ffffff;
  }
  * { box-sizing: border-box; margin: 0; padding: 0; }
  html, body {
    width: 1200px;
    height: 997px;
    overflow: hidden;
    background: var(--backdrop);
  }
  .canvas {
    position: relative;
    width: 1200px;
    height: 997px;
  }
  .card {
    position: absolute;
    left: 240px;
    width: 720px;
    height: 412px;
    background: var(--card);
    box-shadow: 0 12px 30px rgba(0, 0, 0, 0.45);
    overflow: hidden;
  }
  .card--front { top: 58px; }
  .card--back  { top: 527px; }

  .wordmark {
    display: flex;
    align-items: center;
    gap: 18px;
    font-family: "Cinzel", serif;
    font-weight: 600;
    color: var(--brand-blue);
    line-height: 1.1;
  }
  .wordmark__square {
    flex: none;
    background: var(--brand-blue);
  }
  .card--front .wordmark {
    position: absolute;
    inset: 0;
    justify-content: center;
  }
  .card--front .wordmark__square { width: 54px; height: 54px; }
  .card--front .wordmark__name { font-size: 44px; }
  .card--front .wordmark__name span { display: block; font-size: 44px; }

  .card--back .wordmark {
    position: absolute;
    left: 70px;
    top: 62px;
  }
  .card--back .wordmark__square { width: 40px; height: 40px; }
  .card--back .wordmark__name { font-size: 32px; }

  .contact {
    position: absolute;
    left: 300px;
    top: 178px;
    font-family: "Arimo", sans-serif;
  }
  .contact__name {
    font-size: 22px;
    font-weight: 700;
    color: var(--brand-blue);
  }
  .contact__phone {
    display: flex;
    align-items: center;
    gap: 8px;
    margin-top: 8px;
    font-size: 15px;
    color: var(--ink-grey);
  }
  .contact__phone svg { width: 14px; height: 14px; }

  .services {
    position: absolute;
    left: 0;
    right: 0;
    bottom: 0;
    height: 126px;
    background: var(--band-blue);
    padding: 30px 40px 0;
    font-family: "Arimo", sans-serif;
    font-weight: 700;
    font-size: 13px;
    letter-spacing: 0.4px;
    text-transform: uppercase;
    color: var(--band-text);
  }
  .services__row {
    display: flex;
    justify-content: center;
    align-items: center;
    gap: 12px;
    margin-bottom: 18px;
  }
  .services__dot {
    width: 8px;
    height: 8px;
    border-radius: 50%;
    background: var(--accent-red);
  }
</style>
</head>
<body>
<main class="canvas">

  <section class="card card--front" aria-label="Business card front">
    <div class="wordmark">
      <span class="wordmark__square" aria-hidden="true"></span>
      <p class="wordmark__name">Pelton Ridge<span>Heating and Cooling</span></p>
    </div>
  </section>

  <section class="card card--back" aria-label="Business card back">
    <div class="wordmark">
      <span class="wordmark__square" aria-hidden="true"></span>
      <p class="wordmark__name">Pelton Ridge Heating and Cooling</p>
    </div>

    <div class="contact">
      <p class="contact__name">Doug Ferriblen</p>
      <p class="contact__phone">
        <svg viewBox="0 0 24 24" aria-hidden="true">
          <path fill="#d42a2a" d="M6.6 10.8a15.1 15.1 0 0 0 6.6 6.6l2.2-2.2c.3-.3.7-.4 1-.2 1.1.4 2.3.6 3.6.6.6 0 1 .4 1 1V20c0 .6-.4 1-1 1A17 17 0 0 1 3 4c0-.6.4-1 1-1h3.5c.6 0 1 .4 1 1 0 1.3.2 2.5.6 3.6.1.3 0 .7-.2 1z"/>
        </svg>
        555-304-9461
      </p>
    </div>

    <ul class="services" aria-label="Services">
      <li class="services__row">
        <span>Furnace and AC repairs</span>
        <span class="services__dot" aria-hidden="true"></span>
        <span>New furnace and AC installation</span>
        <span class="services__dot" aria-hidden="true"></span>
        <span>Ductwork</span>
      </li>
      <li class="services__row">
        <span>Gas lines</span>
        <span class="services__dot" aria-hidden="true"></span>
        <span>Water tanks</span>
        <span class="services__dot" aria-hidden="true"></span>
        <span>Tankless water heaters</span>
      </li>
    </ul>
  </section>

</main>
</body>
</html>
```